Powerful Design & Selling Tool

We sell health care consulting Services to medical practices (doctors).<br/>we need a powerful design to use as a selling tool that conveys, health care knowledge, expertise professionalism and includes the services we offer. <br/>The design should incorporate our logo and its colors (blue and white). However other colors can be included. I am open to the designer's creativity and color options. you can find our logo on our website at www bright harbor advisory.com. Please feel free to ask questions.

Target Market(s)

Doctors and health care administrators

Industry/Entity Type

Health Care

Colors

Designer to choose colors to be used in the design.

Requirements
Must have
• logo somewhere in the footer
Nice to have
• any creative designs the design wants to add

```html
<!DOCTYPE html>
<html lang="en">
<head>
<meta charset="utf-8">
<title>Bright Harbor Advisory – Presentation Deck</title>
<link href="https://fonts.googleapis.com/css2?family=Nunito+Sans:wght@300;400;600;700;800;900&family=Libre+Baskerville:wght@400;700&display=swap" rel="stylesheet">
<style>
:root{
  --blue:#0c55b0;
  --blue-d:#0a3f86;
  --blue-l:#2f7fd6;
  --sky:#35a4e6;
  --ice:#dff1fb;
  --ink:#3b3f46;
  --mute:#8a8f98;
  --rule:#cfd4dc;
  --page:#e9eaed;
  --white:#ffffff;
}
*{box-sizing:border-box;margin:0;padding:0}
html,body{width:1200px;height:2518px;overflow:hidden}
body{font-family:"Nunito Sans",Arial,sans-serif;color:var(--ink);background:var(--page)}
.canvas{position:relative;width:1200px;height:2518px;overflow:hidden;background:var(--page)}
.abs{position:absolute}

/* hero */
.hero-band{position:absolute;left:0;top:0;width:1200px;height:760px}
.brand{font-family:"Nunito Sans",sans-serif;font-weight:800;color:var(--white);letter-spacing:2px}
.hero-brand{position:absolute;left:204px;top:196px;font-size:60px}
.hero-title{position:absolute;left:70px;top:288px;color:var(--white);font-weight:800;font-size:60px;line-height:1}
.hero-deck{position:absolute;left:196px;top:350px;color:var(--white);font-weight:300;font-size:62px;line-height:1}
.hero-slide{position:absolute;left:560px;top:186px;width:472px;height:266px;background:linear-gradient(135deg,#1a64c4,#0b4ea7);box-shadow:0 18px 40px rgba(10,40,90,.35)}
.hero-slide .brand{position:absolute;top:46px;width:100%;text-align:center;font-size:40px}
.hero-slide .pt{position:absolute;top:148px;width:100%;text-align:center;font-family:"Libre Baskerville",serif;color:#fff;font-size:19px}
.hero-slide .ps{position:absolute;top:174px;width:100%;text-align:center;font-family:"Libre Baskerville",serif;color:#fff;font-size:8px;letter-spacing:.5px}
.hero-rule{position:absolute;left:462px;top:640px;width:254px;height:1px;background:#b8c0cc}
.hero-caption{position:absolute;left:0;width:1200px;top:670px;text-align:center;color:var(--blue);font-weight:300;font-size:33px}

/* grid of slides */
.deck{position:absolute;left:50px;top:769px;display:grid;grid-template-columns:352px 352px 354px;grid-auto-rows:198px;column-gap:21px;row-gap:16px}
.slide{position:relative;background:var(--white);overflow:hidden;box-shadow:0 6px 16px rgba(25,60,120,.18)}
.tab{position:absolute;right:12px;top:0;width:14px;height:13px;background:var(--blue);border-radius:0 0 4px 4px}
.s-title{position:absolute;left:0;right:0;top:16px;text-align:center;font-weight:800;font-size:14px;color:var(--blue)}
.s-sub{position:absolute;left:0;right:0;top:34px;text-align:center;font-size:5px;letter-spacing:2.4px;color:var(--mute)}
.dots{position:absolute;left:50%;top:42px;transform:translateX(-50%);display:flex;gap:2px}
.dots i{display:block;width:3px;height:3px;border-radius:50%;background:#9ccbef}
.dots i:first-child{background:var(--blue)}
.foot{position:absolute;left:8px;right:8px;bottom:6px;height:8px;border-top:.6px solid var(--rule)}
.foot .url{position:absolute;left:0;top:1px;font-size:3.6px;font-weight:700;color:var(--blue)}
.foot .mark{position:absolute;right:4px;top:-2px;font-size:6px;font-weight:800;color:var(--blue)}
.lorem{font-size:4.3px;line-height:1.55;color:#555;text-align:justify}
.h6{font-size:5.4px;font-weight:800;color:var(--blue)}
.photo{position:absolute}
.bluebg{background:var(--blue)}
.cap{font-size:5px;font-weight:700;color:var(--blue)}
.ico{fill:none;stroke:#fff;stroke-width:1.6;stroke-linecap:round;stroke-linejoin:round}
.ico-b{fill:none;stroke:var(--blue);stroke-width:1.4;stroke-linecap:round;stroke-linejoin:round}
.btn{position:absolute;border-radius:8px;font-size:5px;color:#fff;text-align:center;line-height:14px;height:14px}
.vert{position:absolute;color:#fff;font-weight:900;transform:rotate(-90deg);transform-origin:left top;white-space:nowrap}
table.data{border-collapse:collapse;width:100%;font-size:3.8px;color:#555}
table.data th{background:var(--blue);color:#fff;font-weight:700;text-align:left;padding:4px 5px;border-right:1px solid #fff}
table.data th.alt{background:var(--blue-l)}
table.data td{padding:3px 5px;height:16px;border-bottom:.5px solid #e2e5ea}
table.data tr:nth-child(even) td{background:#f3f5f8}
.card{position:absolute;background:#fff;box-shadow:0 2px 6px rgba(0,0,0,.12);padding:6px}
.bul{list-style:none;font-size:3.8px;color:#666;line-height:1.9}
.bul li::before{content:"▸ ";color:var(--blue)}
.np{position:absolute;width:100px}
.np .n{position:absolute;left:0;top:2px;width:11px;height:11px;border-radius:50%;background:var(--blue);color:#fff;font-size:4.5px;font-weight:800;text-align:center;line-height:11px;box-shadow:0 0 0 2px #d6e6f7}
.np .t{position:absolute;left:18px;top:0;width:80px}
.gantt{position:absolute;left:16px;top:62px;width:322px}
.g-head{display:grid;grid-template-columns:74px repeat(12,1fr);gap:1px;height:9px}
.g-head span{background:#3c4250;color:#fff;font-size:4px;text-align:center;line-height:9px}
.g-head span:first-child{background:transparent}
.g-row{display:grid;grid-template-columns:74px 1fr;gap:1px;height:11px;margin-top:1px}
.g-row .lab{background:var(--blue);color:#fff;font-size:3.8px;line-height:11px;padding-left:24px}
.g-row .trk{position:relative;background:#eef1f5}
.g-row .bar{position:absolute;top:3px;height:4px}
.member{position:absolute;width:150px;height:60px}
.member .av{position:absolute;left:0;top:4px;width:38px;height:38px;border-radius:50%;background:radial-gradient(circle at 45% 35%,#9aa0a8,#4a4f57)}
.member .nm{position:absolute;left:48px;top:4px;font-size:5px;font-weight:800;color:var(--blue)}
.member .rl{position:absolute;left:48px;top:11px;font-size:3.8px;color:#888;font-style:italic}
.member .lorem{position:absolute;left:48px;top:18px;width:100px}
.contact{position:absolute;left:30px;font-size:4.6px;color:#444;display:flex;align-items:center;gap:6px}
</style>
</head>
<body>
<div class="canvas">

  <!-- hero -->
  <svg class="hero-band" viewBox="0 0 1200 760" role="img" aria-label="Blue banner with a faint photo of a cheering crowd at sunset">
    <defs>
      <linearGradient id="heroGrad" x1="0" y1="0" x2="1" y2="1">
        <stop offset="0" stop-color="#2b63a8"/>
        <stop offset=".5" stop-color="#1f5aa7"/>
        <stop offset="1" stop-color="#0d4f9f"/>
      </linearGradient>
    </defs>
    <polygon points="0,0 1200,0 1200,68 0,752" fill="url(#heroGrad)"/>
  </svg>
  <div class="brand hero-brand">BHA</div>
  <div class="hero-title">Presentation</div>
  <div class="hero-deck">Deck</div>
  <div class="hero-slide">
    <div class="brand">BHA</div>
    <div class="pt">PRESENTATION TITLE</div>
    <div class="ps">SUB TITLE GOES HERE</div>
  </div>
  <div class="hero-rule"></div>
  <div class="hero-caption">Powerpoint Presentation</div>

  <div class="deck">

    <!-- 1 title -->
    <section class="slide" style="background:linear-gradient(135deg,#1b66c6,#0b4ea6)">
      <div class="brand abs" style="left:0;right:0;top:26px;text-align:center;font-size:30px">BHA</div>
      <div class="abs" style="left:0;right:0;top:104px;text-align:center;font-family:'Libre Baskerville',serif;color:#fff;font-size:12.5px">PRESENTATION TITLE</div>
      <div class="abs" style="left:0;right:0;top:120px;text-align:center;font-family:'Libre Baskerville',serif;color:#fff;font-size:5px">SUB TITLE GOES HERE</div>
    </section>

    <!-- 2 cover with photo -->
    <section class="slide">
      <div class="photo" role="img" aria-label="Faded photo of a medical team meeting" style="inset:0;background:linear-gradient(180deg,#eef1f5,#fafbfc 60%,#fff)"></div>
      <div class="abs" style="left:0;right:0;top:48px;text-align:center;font-weight:800;font-size:18px;color:var(--blue);letter-spacing:1px">BHA</div>
      <div class="abs" style="left:0;right:0;top:70px;text-align:center;font-size:3.8px;color:#777">BRIGHT HARBOR ADVISORY LLC</div>
      <div class="abs" style="left:0;right:0;top:86px;text-align:center;font-family:'Libre Baskerville',serif;color:var(--blue);font-size:12px">PRESENTATION TITLE</div>
      <div class="abs" style="left:0;right:0;top:102px;text-align:center;font-family:'Libre Baskerville',serif;color:var(--blue-l);font-size:4.6px">SUB TITLE GOES HERE</div>
      <p class="lorem abs" style="left:60px;right:52px;top:122px;text-align:center">Lorem ipsum dolor sit amet, consectetur adipiscing elit, sed do eiusmod tempor incididunt ut labore et dolore magna aliqua. Lorem ipsum dolor sit amet, consectetur adipiscing elit, sed do eiusmod tempor incididunt ut labore et dolore magna aliqua.</p>
      <div class="btn bluebg" style="left:138px;top:154px;width:88px">PRESENTER NAME</div>
    </section>

    <!-- 3 agenda -->
    <section class="slide">
      <div class="photo" role="img" aria-label="Soft light blue gradient with faint hexagon texture" style="inset:0;background:linear-gradient(180deg,#fff 35%,#cdeef9)"></div>
      <div class="abs" style="left:22px;top:86px;font-weight:800;font-size:14px;color:var(--blue-d)">Ageda</div>
      <div class="abs" style="left:22px;top:104px;font-size:4.5px;letter-spacing:2px;color:#888">SUB TITLE GOES HERE</div>
      <div class="abs" style="left:22px;top:112px;display:flex;gap:2px"><i style="width:3px;height:3px;border-radius:50%;background:var(--blue)"></i><i style="width:3px;height:3px;border-radius:50%;background:#9ccbef"></i></div>
      <div class="abs" style="left:231px;top:42px;width:1px;height:120px;background:#b9d6ee"></div>
      <div class="abs" style="left:228px;top:38px;font-size:5px;color:var(--blue);line-height:23px">
        <div>○&nbsp; Mission &amp; Vision</div><div>○&nbsp; Our Services</div><div>○&nbsp; Company Profile</div><div>○&nbsp; Project Portfolio</div><div>○&nbsp; Our Team</div><div>○&nbsp; Q&amp;As / Closing Speech</div>
      </div>
    </section>

    <!-- 4 welcome -->
    <section class="slide">
      <div class="abs bluebg" style="left:0;top:0;width:70px;height:198px"></div>
      <div class="vert" style="left:22px;top:156px;font-size:24px">Welcome</div>
      <div class="photo" role="img" aria-label="Photo of two colleagues reviewing work at a table" style="left:70px;top:0;width:143px;height:198px;background:linear-gradient(160deg,#c8b9a6,#6d5a4a 60%,#3a3430)"></div>
      <div class="tab"></div>
      <div class="abs" style="left:226px;top:46px;width:112px">
        <p class="lorem">Lorem ipsum dolor sit amet, consectetur adipiscing elit, sed do eiusmod tempor incididunt ut labore et dolore magna aliqua. Lorem ipsum dolor sit amet, consectetur adipiscing elit, sed do eiusmod tempor incididunt ut labore et dolore magna aliqua.</p>
        <p class="lorem" style="margin-top:5px">Lorem ipsum dolor sit amet, consectetur adipiscing elit, sed do eiusmod tempor incididunt ut labore et dolore magna aliqua. Lorem ipsum dolor sit amet, consectetur adipiscing elit, sed do eiusmod tempor incididunt ut labore et dolore magna aliqua.</p>
      </div>
      <div class="foot" style="left:226px"><span class="mark">BHA</span></div>
    </section>

    <!-- 5 part one -->
    <section class="slide">
      <div class="abs bluebg" style="left:0;top:0;width:50px;height:198px"></div>
      <div class="vert" style="left:14px;top:156px;font-size:20px">PART ONE</div>
      <div class="photo" role="img" aria-label="Photo of a hand writing notes beside a laptop" style="left:188px;top:0;width:164px;height:198px;background:linear-gradient(150deg,#f2f2f0,#d9d7d2 55%,#8d8d8f)"></div>
      <div class="abs bluebg" style="left:158px;top:10px;width:30px;height:22px;color:#fff;font-weight:800;font-size:13px;text-align:center;line-height:22px">01</div>
      <div class="abs" style="left:68px;top:46px;font-weight:800;font-size:13px;color:var(--blue)">Text &amp; Picture</div>
      <div class="abs" style="left:70px;top:64px;font-size:4.5px;letter-spacing:2px;color:#888">SUB TITLE GOES HERE</div>
      <p class="lorem abs" style="left:68px;top:80px;width:110px">Lorem ipsum dolor sit amet, consectetur adipiscing elit, sed do eiusmod tempor incididunt ut labore et dolore magna aliqua. Lorem ipsum dolor sit amet, consectetur adipiscing elit, sed do eiusmod tempor incididunt ut labore et dolore magna aliqua. Ut enim ad minim veniam, quis nostrud exercitation ullamco laboris nisi ut aliquip lorem ipsum dolor sit amet, consectetur adipiscing elit, sed do eiusmod tempor incididunt ut labore et dolore magna aliqua.</p>
      <div class="abs" style="left:50px;top:189px;font-size:3.5px;color:var(--blue)">.com</div>
    </section>

    <!-- 6 awesome text -->
    <section class="slide">
      <div class="tab"></div>
      <div class="s-title">Your Awesome Text</div>
      <div class="s-sub">SUB TITLE GOES HERE</div>
      <div class="dots"><i></i><i></i></div>
      <p class="lorem abs" style="left:48px;right:36px;top:66px;text-align:center">Lorem ipsum dolor sit amet, consectetur adipiscing elit, sed do eiusmod tempor incididunt ut labore et dolore magna aliqua. Ut enim ad minim veniam, quis nostrud exercitation ullamco laboris nisi ut aliquip ex ea commodo consequat. Lorem ipsum dolor sit amet, consectetur adipiscing elit, sed do eiusmod tempor incididunt ut labore et dolore magna aliqua.</p>
      <div class="btn" style="left:54px;top:122px;width:92px;border-radius:3px;background:linear-gradient(180deg,#3a9ae0,#1e7ac8);box-shadow:0 4px 5px rgba(0,0,0,.2)">Innovative Strategies</div>
      <div class="btn" style="left:204px;top:122px;width:92px;border-radius:3px;background:linear-gradient(180deg,#c8cbd0,#9ea3aa);box-shadow:0 4px 5px rgba(0,0,0,.2)">Our Commitment to our Clients</div>
      <div class="foot"><span class="url">www.brightharboradvisory.com</span><span class="mark">BHA</span></div>
    </section>

    <!-- 7 overview -->
    <section class="slide">
      <div class="tab"></div>
      <div class="s-title">Overview</div>
      <div class="s-sub">SUB TITLE GOES HERE</div>
      <div class="dots"><i></i><i></i></div>
      <div class="abs" style="left:24px;right:24px;top:62px">
        <p class="lorem">Lorem ipsum dolor sit amet, consectetur adipiscing elit, sed do eiusmod tempor incididunt ut labore et dolore magna aliqua. Lorem ipsum dolor sit amet, consectetur adipiscing elit, sed do eiusmod tempor incididunt ut labore et dolore magna aliqua. Ut enim ad minim veniam, quis nostrud exercitation ullamco laboris nisi ut aliquip.</p>
        <p class="lorem" style="margin-top:4px">Lorem ipsum dolor sit amet, consectetur adipiscing elit, sed do eiusmod tempor incididunt ut labore et dolore magna aliqua. Lorem ipsum dolor sit amet, consectetur adipiscing elit, sed do eiusmod tempor incididunt ut labore et dolore magna aliqua. Ut enim ad minim veniam, quis nostrud exercitation ullamco laboris nisi ut aliquip.</p>
        <p class="lorem" style="margin-top:4px">Lorem ipsum dolor sit amet, consectetur adipiscing elit, sed do eiusmod tempor incididunt ut labore et dolore magna aliqua. Lorem ipsum dolor sit amet, consectetur adipiscing elit, sed do eiusmod tempor incididunt ut labore et dolore magna aliqua. Ut enim ad minim veniam, quis nostrud exercitation ullamco laboris nisi ut aliquip. Lorem ipsum dolor sit amet, consectetur adipiscing elit, sed do eiusmod tempor incididunt ut labore et dolore magna aliqua.</p>
      </div>
      <div class="foot"><span class="url">www.brightharboradvisory.com</span><span class="mark">BHA</span></div>
    </section>

    <!-- 8 two column -->
    <section class="slide">
      <div class="tab"></div>
      <div class="s-title">Two Column Text</div>
      <div class="s-sub">SUB TITLE GOES HERE</div>
      <div class="dots"><i></i><i></i></div>
      <div class="abs" style="left:30px;top:66px;width:142px">
        <p class="lorem">Lorem ipsum dolor sit amet, consectetur adipiscing elit, sed do eiusmod tempor incididunt ut labore et dolore magna aliqua. Lorem ipsum dolor sit amet, consectetur adipiscing elit, sed do eiusmod tempor incididunt ut labore et dolore magna aliqua. Ut enim ad minim veniam, quis nostrud exercitation ullamco laboris nisi ut aliquip.</p>
        <p class="lorem" style="margin-top:5px">Lorem ipsum dolor sit amet, consectetur adipiscing elit, sed do eiusmod tempor incididunt ut labore et dolore magna aliqua. Lorem ipsum dolor sit amet, consectetur adipiscing elit, sed do eiusmod tempor incididunt ut labore et dolore magna aliqua.</p>
      </div>
      <div class="abs" style="left:190px;top:66px;width:142px">
        <p class="lorem">Lorem ipsum dolor sit amet, consectetur adipiscing elit, sed do eiusmod tempor incididunt ut labore et dolore magna aliqua. Lorem ipsum dolor sit amet, consectetur adipiscing elit, sed do eiusmod tempor incididunt ut labore et dolore magna aliqua.</p>
        <p class="lorem" style="margin-top:5px">Ut enim ad minim veniam, quis nostrud exercitation ullamco laboris nisi ut aliquip lorem ipsum dolor sit amet, consectetur adipiscing elit, sed do eiusmod tempor incididunt ut labore et dolore magna aliqua. Lorem ipsum dolor sit amet, consectetur adipiscing elit, sed do eiusmod tempor incididunt ut labore et dolore magna aliqua.</p>
      </div>
      <div class="foot"><span class="url">www.brightharboradvisory.com</span><span class="mark">BHA</span></div>
    </section>

    <!-- 9 company -->
    <section class="slide">
      <div class="tab"></div>
      <div class="s-title">Bright Harbor Advisory</div>
      <div class="s-sub">SUB TITLE GOES HERE</div>
      <div class="dots"><i></i><i></i></div>
      <div class="abs" style="left:18px;top:50px;width:314px;height:136px;background:#f1f3f6;border-radius:6px"></div>
      <div class="photo" role="img" aria-label="Photo of a smiling doctor holding a stethoscope" style="left:20px;top:48px;width:82px;height:122px;border-radius:8px;background:linear-gradient(160deg,#e9e4df,#c7a898 55%,#8e6f63);box-shadow:0 3px 8px rgba(0,0,0,.2)"></div>
      <div class="abs" style="left:282px;top:36px;width:52px;height:52px;border-radius:50%;background:var(--sky);box-shadow:0 0 0 4px #bfe3f7;color:#fff;text-align:center">
        <div style="font-weight:800;font-size:8px;margin-top:12px">50%</div>
        <div style="font-size:3.5px;line-height:1.3;padding:0 6px">Lorem ipsum dolor sit amet, consectetur adipiscing</div>
      </div>
      <p class="lorem abs" style="left:112px;top:86px;width:188px;text-align:left">Bright Harbor Advisory (BHA), founded in 2015, is a Management Service Organization &amp; Healthcare Consulting Firm skilled at helping medical practices advance their strategic vision in an ever-evolving healthcare system. Bright Harbor Advisory specializes in Revenue Cycle Management, Practice Management, Compliance Management &amp; Healthcare Innovation. The expertise of our team &amp; our strategic approach allows us to dig deep, make assessments, innovate, develop &amp; implement solutions that will advance your practice, designing strategies and solutions that advance operations while also preserving your organization's mission, vision, and strategic initiatives.</p>
      <div class="foot"><span class="url">www.brightharboradvisory.com</span><span class="mark">BHA</span></div>
    </section>

    <!-- 10 three column cards -->
    <section class="slide">
      <div class="tab"></div>
      <div class="s-title">Three Column Text</div>
      <div class="s-sub">SUB TITLE GOES HERE</div>
      <div class="dots"><i></i><i></i></div>
      <p class="lorem abs" style="left:20px;right:20px;top:60px;text-align:center">Lorem ipsum dolor sit amet, consectetur adipiscing elit, sed do eiusmod tempor incididunt ut labore et dolore magna aliqua. Sed do eiusmod tempor incididunt ut labore et dolore magna aliqua. Lorem ipsum dolor sit amet, consectetur adipiscing elit.</p>
      <div class="abs" style="left:0;right:0;top:78px;height:98px;background:#eef0f4"></div>
      <div class="card" style="left:12px;top:90px;width:104px;height:82px"><div class="h6">Lorem ipsum dolor</div><p class="lorem" style="margin-top:2px">Lorem ipsum dolor sit amet, consectetur adipiscing elit, sed do eiusmod tempor</p><ul class="bul"><li>Lorem ipsum dolor</li><li>Sit amet consectetur adipiscing</li><li>Do eiusmod tempor</li><li>Et pero ipsum do</li><li>Lorem ipsum dolor</li></ul></div>
      <div class="card" style="left:124px;top:90px;width:104px;height:82px"><div class="h6">Lorem ipsum dolor</div><p class="lorem" style="margin-top:2px">Lorem ipsum dolor sit amet, consectetur adipiscing elit, sed do eiusmod tempor</p><ul class="bul"><li>Lorem ipsum dolor</li><li>Sit amet consectetur adipiscing</li><li>Do eiusmod tempor</li><li>Et pero ipsum do</li><li>Lorem ipsum dolor</li></ul></div>
      <div class="card" style="left:236px;top:90px;width:104px;height:82px"><div class="h6">Lorem ipsum dolor</div><p class="lorem" style="margin-top:2px">Lorem ipsum dolor sit amet, consectetur adipiscing elit, sed do eiusmod tempor</p><ul class="bul"><li>Lorem ipsum dolor</li><li>Sit amet consectetur adipiscing</li><li>Do eiusmod tempor</li><li>Et pero ipsum do</li><li>Lorem ipsum dolor</li></ul></div>
      <div class="foot"><span class="url">www.brightharboradvisory.com</span><span class="mark">BHA</span></div>
    </section>

    <!-- 11 table -->
    <section class="slide">
      <div class="tab"></div>
      <div class="s-title">Table Slide</div>
      <div class="s-sub">SUB TITLE GOES HERE</div>
      <div class="dots"><i></i><i></i></div>
      <div class="abs" style="left:16px;right:14px;top:58px">
        <table class="data">
          <tr><th style="width:18px">No</th><th style="width:106px">Example text</th><th class="alt">Example text</th><th>Example text</th><th class="alt">Example text</th></tr>
          <tr><td>1</td><td>Lorem ipsum dolor sit amet, consectetur adipiscing elit, sed do eiusmod tempor</td><td>100 %</td><td>120 USD</td><td>1M</td></tr>
          <tr><td>2</td><td>Lorem ipsum dolor sit amet, consectetur adipiscing elit, sed do eiusmod tempor</td><td>100 %</td><td>250 USD</td><td>3M</td></tr>
          <tr><td>3</td><td>Lorem ipsum dolor sit amet, consectetur adipiscing elit, sed do eiusmod tempor</td><td>100 %</td><td>225 USD</td><td>5M</td></tr>
          <tr><td>4</td><td>Lorem ipsum dolor sit amet, consectetur adipiscing elit, sed do eiusmod tempor</td><td>100 %</td><td>100 USD</td><td>1M</td></tr>
          <tr><td>5</td><td>Lorem ipsum dolor sit amet, consectetur adipiscing elit, sed do eiusmod tempor</td><td>100 %</td><td>125 USD</td><td>2M</td></tr>
        </table>
      </div>
      <div class="foot"><span class="url">www.brightharboradvisory.com</span><span class="mark">BHA</span></div>
    </section>

    <!-- 12 three column with circle -->
    <section class="slide">
      <div class="tab"></div>
      <div class="s-title">Three Column Text</div>
      <div class="s-sub">SUB TITLE GOES HERE</div>
      <div class="dots"><i></i><i></i></div>
      <div class="abs bluebg" style="left:36px;top:80px;width:78px;height:78px;border-radius:50%;color:#fff;font-weight:800;font-size:18px;text-align:center;line-height:78px">BHA</div>
      <svg class="abs" style="left:150px;top:62px" width="200" height="120" viewBox="0 0 200 120">
        <path d="M12 10 A60 60 0 0 0 12 110" fill="none" stroke="#dbe8f6" stroke-width="1"/>
        <g><circle cx="24" cy="16" r="11" fill="#c9dff3"/><circle cx="24" cy="16" r="7.5" fill="#e4eff9"/></g>
        <g><circle cx="10" cy="58" r="11" fill="#c9dff3"/><circle cx="10" cy="58" r="7.5" fill="#e4eff9"/></g>
        <g><circle cx="24" cy="100" r="11" fill="#c9dff3"/><circle cx="24" cy="100" r="7.5" fill="#e4eff9"/></g>
        <circle cx="24" cy="16" r="3.5" class="ico-b"/>
        <circle cx="10" cy="56" r="2" class="ico-b"/><path d="M6.5 62 q3.5-4 7 0" class="ico-b"/>
        <path d="M20 103 l3-4 3 2 4-5" class="ico-b"/>
      </svg>
      <div class="abs" style="left:194px;top:70px;width:140px"><div class="h6">Lorem ipsum dolor</div><p class="lorem">Lorem ipsum dolor sit amet, nec an dolore equidem appetere ut nec commune.</p></div>
      <div class="abs" style="left:180px;top:112px;width:150px"><div class="h6">Lorem ipsum dolor</div><p class="lorem">Lorem ipsum dolor sit amet, nec an dolore equidem appetere ut nec commune.</p></div>
      <div class="abs" style="left:194px;top:154px;width:140px"><div class="h6">Lorem ipsum dolor</div><p class="lorem">Lorem ipsum dolor sit amet, nec an dolore equidem appetere ut nec commune.</p></div>
      <div class="foot"><span class="url">www.brightharboradvisory.com</span><span class="mark">BHA</span></div>
    </section>

    <!-- 13 ring diagram -->
    <section class="slide">
      <div class="tab"></div>
      <div class="s-title">Two Column Text</div>
      <div class="s-sub">SUB TITLE GOES HERE</div>
      <div class="dots"><i></i><i></i></div>
      <svg class="abs" style="left:116px;top:58px" width="120" height="120" viewBox="0 0 120 120">
        <g fill="none" stroke-width="22" transform="rotate(-90 60 60)">
          <circle cx="60" cy="60" r="41" stroke="#0c55b0" stroke-dasharray="40 218"/>
          <circle cx="60" cy="60" r="41" stroke="#9fd1f0" stroke-dasharray="40 218" stroke-dashoffset="-43"/>
          <circle cx="60" cy="60" r="41" stroke="#35a4e6" stroke-dasharray="40 218" stroke-dashoffset="-86"/>
          <circle cx="60" cy="60" r="41" stroke="#0c55b0" stroke-dasharray="40 218" stroke-dashoffset="-129"/>
          <circle cx="60" cy="60" r="41" stroke="#cfe6f7" stroke-dasharray="40 218" stroke-dashoffset="-172"/>
          <circle cx="60" cy="60" r="41" stroke="#35a4e6" stroke-dasharray="40 218" stroke-dashoffset="-215"/>
        </g>
        <circle cx="88" cy="32" r="4" class="ico"/><circle cx="60" cy="19" r="3" class="ico"/><path d="M88 90 l-3 4 h6z" class="ico"/><path d="M30 88 c-3-3 3-7 5-3" class="ico"/><circle cx="21" cy="60" r="3" class="ico"/><path d="M98 58 h4 v5 h-4z" class="ico"/>
      </svg>
      <div class="abs" style="left:40px;top:58px;width:78px;text-align:right"><div class="h6" style="font-size:4.8px">Lorem ipsum dolor</div><p class="lorem" style="text-align:right">Lorem ipsum dolor sit amet, consectetur adipiscing elit, sed do eiusmod tempor</p></div>
      <div class="abs" style="left:22px;top:108px;width:80px;text-align:right"><div class="h6" style="font-size:4.8px">Lorem ipsum dolor</div><p class="lorem" style="text-align:right">Lorem ipsum dolor sit amet, consectetur adipiscing elit, sed do eiusmod tempor</p></div>
      <div class="abs" style="left:40px;top:156px;width:78px;text-align:right"><div class="h6" style="font-size:4.8px">Lorem ipsum dolor</div><p class="lorem" style="text-align:right">Lorem ipsum dolor sit amet, consectetur adipiscing elit, sed do eiusmod tempor</p></div>
      <div class="abs" style="left:226px;top:56px;width:84px"><div class="h6" style="font-size:4.8px">Lorem ipsum dolor</div><p class="lorem">Lorem ipsum dolor sit amet, consectetur adipiscing elit, sed do eiusmod tempor</p></div>
      <div class="abs" style="left:244px;top:106px;width:84px"><div class="h6" style="font-size:4.8px">Lorem ipsum dolor</div><p class="lorem">Lorem ipsum dolor sit amet, consectetur adipiscing elit, sed do eiusmod tempor</p></div>
      <div class="abs" style="left:226px;top:156px;width:84px"><div class="h6" style="font-size:4.8px">Lorem ipsum dolor</div><p class="lorem">Lorem ipsum dolor sit amet, consectetur adipiscing elit, sed do eiusmod tempor</p></div>
      <div class="foot"><span class="url">www.brightharboradvisory.com</span><span class="mark">BHA</span></div>
    </section>

    <!-- 14 four points -->
    <section class="slide">
      <div class="tab"></div>
      <div class="s-title">Four Points</div>
      <div class="s-sub">SUB TITLE GOES HERE</div>
      <div class="dots"><i></i><i></i></div>
      <svg class="abs" style="left:24px;top:76px" width="310" height="84" viewBox="0 0 310 84">
        <g fill="none" stroke-width="6">
          <circle cx="42" cy="42" r="35" stroke="#0c55b0"/>
          <circle cx="113" cy="42" r="35" stroke="#35a4e6"/>
          <circle cx="184" cy="42" r="35" stroke="#0c55b0"/>
          <circle cx="255" cy="42" r="35" stroke="#35a4e6"/>
        </g>
        <g fill="none" stroke="#cfe3f4" stroke-width="1">
          <circle cx="42" cy="42" r="29"/><circle cx="113" cy="42" r="29"/><circle cx="184" cy="42" r="29"/><circle cx="255" cy="42" r="29"/>
        </g>
      </svg>
      <div class="abs" style="left:44px;top:102px;width:44px;font-size:3.8px;line-height:1.5;color:#666;text-align:center">Lorem ipsum is simply dummy unknown printer took a galley of type and scrambled it to make.</div>
      <div class="abs" style="left:115px;top:102px;width:44px;font-size:3.8px;line-height:1.5;color:#666;text-align:center">Lorem ipsum is simply dummy unknown printer took a galley of type and scrambled it to make.</div>
      <div class="abs" style="left:186px;top:102px;width:44px;font-size:3.8px;line-height:1.5;color:#666;text-align:center">Lorem ipsum is simply dummy unknown printer took a galley of type and scrambled it to make.</div>
      <div class="abs" style="left:257px;top:102px;width:44px;font-size:3.8px;line-height:1.5;color:#666;text-align:center">Lorem ipsum is simply dummy unknown printer took a galley of type and scrambled it to make.</div>
      <div class="foot"><span class="url">www.brightharboradvisory.com</span><span class="mark">BHA</span></div>
    </section>

    <!-- 15 arcs -->
    <section class="slide">
      <div class="tab"></div>
      <svg class="abs" style="left:30px;top:68px" width="300" height="80" viewBox="0 0 300 80">
        <g fill="none" stroke-width="7">
          <path d="M6 38 A28 28 0 0 0 62 38" stroke="#0c55b0"/>
          <path d="M62 38 A28 28 0 0 1 118 38" stroke="#35a4e6"/>
          <path d="M118 38 A28 28 0 0 0 174 38" stroke="#0c55b0"/>
          <path d="M174 38 A28 28 0 0 1 230 38" stroke="#35a4e6"/>
          <path d="M230 38 A28 28 0 0 0 286 38" stroke="#0c55b0"/>
        </g>
        <g>
          <circle cx="34" cy="38" r="14" fill="#0c55b0"/><circle cx="90" cy="38" r="14" fill="#35a4e6"/><circle cx="146" cy="38" r="14" fill="#0c55b0"/><circle cx="202" cy="38" r="14" fill="#35a4e6"/><circle cx="258" cy="38" r="14" fill="#0c55b0"/>
        </g>
        <circle cx="34" cy="38" r="5" class="ico"/><circle cx="90" cy="38" r="5" class="ico"/><circle cx="90" cy="38" r="2" class="ico"/><path d="M141 40 q5 6 10 0" class="ico"/><path d="M198 32 h8 v12 h-8z" class="ico"/><path d="M252 33 h12 v10 h-12z M258 35 v6 M255 38 h6" class="ico"/>
      </svg>
      <div class="abs" style="left:84px;top:28px;width:80px;text-align:center"><div class="cap" style="font-size:4.2px;color:#333">Your Contents Here</div><p class="lorem" style="text-align:center">Lorem ipsum dolor sit amet, consectetur adipiscing elit, sed do eiusmod tempor incididunt ut labore et dolore magna aliqua.</p></div>
      <div class="abs" style="left:196px;top:28px;width:80px;text-align:center"><div class="cap" style="font-size:4.2px;color:#333">Your Contents Here</div><p class="lorem" style="text-align:center">Lorem ipsum dolor sit amet, consectetur adipiscing elit, sed do eiusmod tempor incididunt ut labore et dolore magna aliqua.</p></div>
      <div class="abs" style="left:24px;top:136px;width:80px;text-align:center"><div class="cap" style="font-size:4.2px;color:#333">Your Contents Here</div><p class="lorem" style="text-align:center">Lorem ipsum dolor sit amet, consectetur adipiscing elit, sed do eiusmod tempor incididunt ut labore et dolore magna aliqua.</p></div>
      <div class="abs" style="left:136px;top:136px;width:80px;text-align:center"><div class="cap" style="font-size:4.2px;color:#333">Your Contents Here</div><p class="lorem" style="text-align:center">Lorem ipsum dolor sit amet, consectetur adipiscing elit, sed do eiusmod tempor incididunt ut labore et dolore magna aliqua.</p></div>
      <div class="abs" style="left:248px;top:136px;width:80px;text-align:center"><div class="cap" style="font-size:4.2px;color:#333">Your Contents Here</div><p class="lorem" style="text-align:center">Lorem ipsum dolor sit amet, consectetur adipiscing elit, sed do eiusmod tempor incididunt ut labore et dolore magna aliqua.</p></div>
      <div class="foot"><span class="url">www.brightharboradvisory.com</span><span class="mark">BHA</span></div>
    </section>

    <!-- 16 nine points -->
    <section class="slide">
      <div class="tab"></div>
      <div class="s-title">Nine Points</div>
      <div class="s-sub">SUB TITLE GOES HERE</div>
      <div class="dots"><i></i><i></i></div>
      <div class="np" style="left:16px;top:62px"><span class="n">01</span><div class="t"><div class="cap" style="color:#333;font-size:4.2px">Project name</div><p class="lorem" style="text-align:left">Lorem ipsum is simply dummy unknown printer took a galley of type and scrambled it to make.</p></div></div>
      <div class="np" style="left:130px;top:62px"><span class="n">04</span><div class="t"><div class="cap" style="color:#333;font-size:4.2px">Project name</div><p class="lorem" style="text-align:left">Lorem ipsum is simply dummy unknown printer took a galley of type and scrambled it to make.</p></div></div>
      <div class="np" style="left:244px;top:62px"><span class="n">07</span><div class="t"><div class="cap" style="color:#333;font-size:4.2px">Project name</div><p class="lorem" style="text-align:left">Lorem ipsum is simply dummy unknown printer took a galley of type and scrambled it to make.</p></div></div>
      <div class="np" style="left:16px;top:100px"><span class="n">02</span><div class="t"><div class="cap" style="color:#333;font-size:4.2px">Project name</div><p class="lorem" style="text-align:left">Lorem ipsum is simply dummy unknown printer took a galley of type and scrambled it to make.</p></div></div>
      <div class="np" style="left:130px;top:100px"><span class="n">05</span><div class="t"><div class="cap" style="color:#333;font-size:4.2px">Project name</div><p class="lorem" style="text-align:left">Lorem ipsum is simply dummy unknown printer took a galley of type and scrambled it to make.</p></div></div>
      <div class="np" style="left:244px;top:100px"><span class="n">08</span><div class="t"><div class="cap" style="color:#333;font-size:4.2px">Project name</div><p class="lorem" style="text-align:left">Lorem ipsum is simply dummy unknown printer took a galley of type and scrambled it to make.</p></div></div>
      <div class="np" style="left:16px;top:138px"><span class="n">03</span><div class="t"><div class="cap" style="color:#333;font-size:4.2px">Project name</div><p class="lorem" style="text-align:left">Lorem ipsum is simply dummy unknown printer took a galley of type and scrambled it to make.</p></div></div>
      <div class="np" style="left:130px;top:138px"><span class="n">06</span><div class="t"><div class="cap" style="color:#333;font-size:4.2px">Project name</div><p class="lorem" style="text-align:left">Lorem ipsum is simply dummy unknown printer took a galley of type and scrambled it to make.</p></div></div>
      <div class="np" style="left:244px;top:138px"><span class="n">09</span><div class="t"><div class="cap" style="color:#333;font-size:4.2px">Project name</div><p class="lorem" style="text-align:left">Lorem ipsum is simply dummy unknown printer took a galley of type and scrambled it to make.</p></div></div>
      <div class="foot"><span class="url">www.brightharboradvisory.com</span><span class="mark">BHA</span></div>
    </section>

    <!-- 17 text and bullets center card -->
    <section class="slide">
      <div class="tab"></div>
      <div class="s-title">Text and Bullet Points</div>
      <div class="s-sub">SUB TITLE GOES HERE</div>
      <div class="dots"><i></i><i></i></div>
      <div class="abs" style="left:18px;top:54px;width:92px">
        <p class="lorem">Lorem ipsum dolor sit amet, consectetur adipiscing elit, sed do eiusmod tempor incididunt ut labore et dolore magna aliqua. Ut enim ad minim veniam, quis nostrud exercitation ullamco laboris nisi ut aliquip.</p>
        <p class="lorem" style="margin-top:5px">Ex commodo consequat. Lorem ipsum dolor sit amet, consectetur adipiscing elit, sed do eiusmod tempor incididunt ut labore et dolore magna aliqua.</p>
        <p class="lorem" style="margin-top:5px">Lorem ipsum dolor sit amet, consectetur adipiscing elit, sed do eiusmod tempor incididunt ut labore et dolore magna aliqua.</p>
      </div>
      <div class="abs" style="left:130px;top:54px;width:92px"><p class="lorem">Lorem ipsum dolor sit amet, consectetur adipiscing elit, sed do eiusmod tempor incididunt ut labore et dolore magna aliqua. Ut enim ad minim veniam, quis nostrud exercitation ullamco.</p></div>
      <div class="abs bluebg" style="left:130px;top:96px;width:94px;height:102px;color:#fff;text-align:center;padding:8px 7px">
        <div style="font-weight:800;font-size:11px">BHA</div>
        <div style="font-size:5px;font-weight:700;margin-top:3px">Lorem ipsum dolor</div>
        <p style="font-size:3.8px;line-height:1.5;margin-top:3px">Lorem ipsum dolor sit amet, consectetur adipiscing elit, sed do eiusmod tempor incididunt ut labore et dolore magna aliqua. Ut enim ad minim veniam, quis nostrud exercitation ullamco laboris nisi ut ex ea commodo consequat.</p>
      </div>
      <div class="abs" style="left:242px;top:54px;width:92px">
        <p class="lorem">Lorem ipsum dolor sit amet, consectetur adipiscing elit, sed do eiusmod tempor incididunt ut labore et dolore magna aliqua. Lorem ipsum dolor sit amet, consectetur adipiscing elit, sed do eiusmod tempor incididunt ut labore et dolore magna aliqua.</p>
        <div style="margin-top:8px;display:grid;gap:9px">
          <div style="display:flex;gap:5px"><span style="color:var(--blue);font-size:7px">▶</span><p class="lorem">Lorem ipsum dolor sit amet, consectetur adipiscing elit, sed do eiusmod tempor</p></div>
          <div style="display:flex;gap:5px"><span style="color:var(--blue);font-size:7px">▶</span><p class="lorem">Lorem ipsum dolor sit amet, consectetur adipiscing elit, sed do eiusmod tempor</p></div>
          <div style="display:flex;gap:5px"><span style="color:var(--blue);font-size:7px">▶</span><p class="lorem">Lorem ipsum dolor sit amet, consectetur adipiscing elit, sed do eiusmod tempor</p></div>
        </div>
      </div>
      <div class="foot"><span class="url">www.brightharboradvisory.com</span><span class="mark">BHA</span></div>
    </section>

    <!-- 18 text and bullets three blue cards -->
    <section class="slide">
      <div class="tab"></div>
      <div class="s-title">Text and Bullet Points</div>
      <div class="s-sub">SUB TITLE GOES HERE</div>
      <div class="dots"><i></i><i></i></div>
      <div class="abs" role="img" aria-label="Blue tinted photo panel with a trophy icon" style="left:18px;top:55px;width:92px;height:118px;background:linear-gradient(160deg,#2a70c8,#0c55b0);color:#fff;text-align:center;padding:8px 6px">
        <svg width="20" height="20" viewBox="0 0 20 20"><path d="M6 3 h8 v5 a4 4 0 0 1-8 0z M10 12 v3 M7 17 h6 M6 5 h-3 a3 3 0 0 0 3 4 M14 5 h3 a3 3 0 0 1-3 4" class="ico"/></svg>
        <div style="font-size:5px;font-weight:700;margin-top:4px">Lorem ipsum dolor</div>
        <p style="font-size:3.8px;line-height:1.5;margin-top:3px;text-align:justify">Lorem ipsum dolor sit amet, consectetur adipiscing elit, sed do eiusmod tempor incididunt ut labore et dolore magna aliqua. Lorem ipsum dolor sit amet, consectetur adipiscing elit, sed do eiusmod tempor incididunt ut labore et dolore magna aliqua.</p>
      </div>
      <div class="abs" role="img" aria-label="Blue tinted photo panel with a paper plane icon" style="left:132px;top:55px;width:92px;height:118px;background:linear-gradient(160deg,#2a70c8,#0c55b0);color:#fff;text-align:center;padding:8px 6px">
        <svg width="20" height="20" viewBox="0 0 20 20"><path d="M3 10 L17 3 L12 17 L9 11z M9 11 L17 3" class="ico"/></svg>
        <div style="font-size:5px;font-weight:700;margin-top:4px">Lorem ipsum dolor</div>
        <p style="font-size:3.8px;line-height:1.5;margin-top:3px;text-align:justify">Lorem ipsum dolor sit amet, consectetur adipiscing elit, sed do eiusmod tempor incididunt ut labore et dolore magna aliqua. Lorem ipsum dolor sit amet, consectetur adipiscing elit, sed do eiusmod tempor incididunt ut labore et dolore magna aliqua.</p>
      </div>
      <div class="abs" role="img" aria-label="Blue tinted photo panel with a caring hands icon" style="left:246px;top:55px;width:92px;height:118px;background:linear-gradient(160deg,#2a70c8,#0c55b0);color:#fff;text-align:center;padding:8px 6px">
        <svg width="20" height="20" viewBox="0 0 20 20"><circle cx="10" cy="7" r="3" class="ico"/><path d="M3 12 q3 5 7 5 q4 0 7-5" class="ico"/></svg>
        <div style="font-size:5px;font-weight:700;margin-top:4px">Lorem ipsum dolor</div>
        <p style="font-size:3.8px;line-height:1.5;margin-top:3px;text-align:justify">Lorem ipsum dolor sit amet, consectetur adipiscing elit, sed do eiusmod tempor incididunt ut labore et dolore magna aliqua. Lorem ipsum dolor sit amet, consectetur adipiscing elit, sed do eiusmod tempor incididunt ut labore et dolore magna aliqua.</p>
      </div>
      <div class="foot"><span class="url">www.brightharboradvisory.com</span><span class="mark">BHA</span></div>
    </section>

    <!-- 19 how can we help -->
    <section class="slide">
      <div class="abs bluebg" style="left:0;top:0;right:0;height:76px"></div>
      <div class="s-title" style="color:#fff;top:14px">How Can We Help You?</div>
      <div class="s-sub" style="color:#cfe0f5;top:32px">SUB TITLE GOES HERE</div>
      <div class="dots" style="top:40px"><i style="background:#fff"></i><i style="background:#9ccbef"></i></div>
      <svg class="abs" style="left:0;top:62px" width="352" height="30" viewBox="0 0 352 30">
        <g fill="#fff" stroke="#d6e6f7" stroke-width="3"><circle cx="68" cy="14" r="12"/><circle cx="142" cy="14" r="12"/><circle cx="218" cy="14" r="12"/><circle cx="292" cy="14" r="12"/></g>
        <circle cx="68" cy="14" r="5" class="ico-b"/><path d="M138 10 h8 v8 h-8z" class="ico-b"/><path d="M213 14 h10 M218 9 v10" class="ico-b"/><circle cx="292" cy="12" r="3" class="ico-b"/><path d="M287 19 q5-4 10 0" class="ico-b"/>
      </svg>
      <div class="abs" style="left:40px;top:96px;width:56px;text-align:center;font-size:4px;font-weight:800;color:var(--blue)">REVENUE CYCLE<br>MANAGEMENT</div>
      <div class="abs" style="left:114px;top:96px;width:56px;text-align:center;font-size:4px;font-weight:800;color:var(--blue)">COMPLIANCE<br>MANAGEMENT</div>
      <div class="abs" style="left:190px;top:96px;width:56px;text-align:center;font-size:4px;font-weight:800;color:var(--blue)">HEALTHCARE<br>INNOVATION</div>
      <div class="abs" style="left:264px;top:96px;width:56px;text-align:center;font-size:4px;font-weight:800;color:var(--blue)">PRACTICE<br>MANAGEMENT</div>
      <p class="lorem abs" style="left:38px;top:112px;width:60px">Partners at Bright Harbor Advisory understand the reimbursement landscape and are skilled in helping medical practices improve their margins. We can help you with medical billing &amp; coding, credentialing, A/R management &amp; staff training.</p>
      <p class="lorem abs" style="left:112px;top:112px;width:60px">In a heavily regulated healthcare environment, medical practices need to be acutely aware of regulations or face huge fines. BHA can help you with risk assessments, compliance plans, clinical documentation audits, safety procedures &amp; staff training.</p>
      <p class="lorem abs" style="left:188px;top:112px;width:60px">Do you want to enhance clinical operations and workflows? Are you looking to expand patient access and improve margins? BHA can help you integrate new technology into your practice including tele-medicine, service desk solutions &amp; more.</p>
      <p class="lorem abs" style="left:262px;top:112px;width:60px">Practice Management requires the right balance of skill, knowledge, management &amp; business expertise. BHA can help strategically grow your practice by expanding patient access, optimizing scheduling, enhancing the patient experience &amp; your online reputation.</p>
      <div class="foot"><span class="url">www.brightharboradvisory.com</span><span class="mark">BHA</span></div>
    </section>

    <!-- 20 our team -->
    <section class="slide">
      <div class="tab"></div>
      <div class="s-title">Our Team</div>
      <div class="s-sub">SUB TITLE GOES HERE</div>
      <div class="dots"><i></i><i></i></div>
      <div class="member" style="left:24px;top:58px"><div class="av" role="img" aria-label="Team member portrait"></div><div class="nm">INSERT NAME</div><div class="rl">Creative Director</div><p class="lorem" style="text-align:left">Lorem ipsum dolor sit amet, consectetur adipiscing elit, sed do eiusmod tempor incididunt ut labore et dolore magna aliqua.</p></div>
      <div class="member" style="left:192px;top:58px"><div class="av" role="img" aria-label="Team member portrait"></div><div class="nm">INSERT NAME</div><div class="rl">Graphic Designer</div><p class="lorem" style="text-align:left">Lorem ipsum dolor sit amet, consectetur adipiscing elit, sed do eiusmod tempor incididunt ut labore et dolore magna aliqua.</p></div>
      <div class="member" style="left:24px;top:126px"><div class="av" role="img" aria-label="Team member portrait"></div><div class="nm">INSERT NAME</div><div class="rl">Account Manager</div><p class="lorem" style="text-align:left">Lorem ipsum dolor sit amet, consectetur adipiscing elit, sed do eiusmod tempor incididunt ut labore et dolore magna aliqua.</p></div>
      <div class="member" style="left:192px;top:126px"><div class="av" role="img" aria-label="Team member portrait"></div><div class="nm">INSERT NAME</div><div class="rl">UI/UX Designer</div><p class="lorem" style="text-align:left">Lorem ipsum dolor sit amet, consectetur adipiscing elit, sed do eiusmod tempor incididunt ut labore et dolore magna aliqua.</p></div>
      <div class="foot"><span class="url">www.brightharboradvisory.com</span><span class="mark">BHA</span></div>
    </section>

    <!-- 21 timeline -->
    <section class="slide">
      <div class="tab"></div>
      <div class="s-title">Timeline</div>
      <div class="s-sub">SUB TITLE GOES HERE</div>
      <div class="dots"><i></i><i></i></div>
      <div class="gantt">
        <div class="g-head"><span></span><span>1</span><span>2</span><span>3</span><span>4</span><span>5</span><span>6</span><span>7</span><span>8</span><span>9</span><span>10</span><span>11</span><span>12</span></div>
        <div class="g-row"><div class="lab">Contents Type</div><div class="trk"><span class="bar" style="left:5%;width:30%;background:#9fd1f0"></span></div></div>
        <div class="g-row"><div class="lab">Contents Type</div><div class="trk"><span class="bar" style="left:28%;width:40%;background:#35a4e6"></span></div></div>
        <div class="g-row"><div class="lab">Contents Type</div><div class="trk"><span class="bar" style="left:18%;width:62%;background:#0a2f6b"></span></div></div>
        <div class="g-row"><div class="lab">Contents Type</div><div class="trk"><span class="bar" style="left:55%;width:32%;background:#0c55b0"></span></div></div>
        <div class="g-row"><div class="lab">Contents Type</div><div class="trk"><span class="bar" style="left:8%;width:72%;background:#2f7fd6"></span></div></div>
        <div class="g-row"><div class="lab">Contents Type</div><div class="trk"><span class="bar" style="left:62%;width:36%;background:#cfe6f7"></span></div></div>
        <div style="display:flex;gap:14px;margin-top:6px;padding-left:20px;font-size:3.5px;color:#666">
          <span><i style="display:inline-block;width:5px;height:4px;background:#9fd1f0"></i> Contents A</span><span><i style="display:inline-block;width:5px;height:4px;background:#35a4e6"></i> Contents B</span><span><i style="display:inline-block;width:5px;height:4px;background:#0a2f6b"></i> Contents C</span><span><i style="display:inline-block;width:5px;height:4px;background:#0c55b0"></i> Contents D</span><span><i style="display:inline-block;width:5px;height:4px;background:#2f7fd6"></i> Contents E</span><span><i style="display:inline-block;width:5px;height:4px;background:#cfe6f7"></i> Contents F</span>
        </div>
      </div>
      <div class="foot"><span class="url">www.brightharboradvisory.com</span><span class="mark">BHA</span></div>
    </section>

    <!-- 22 revenue cycle -->
    <section class="slide">
      <div class="photo" role="img" aria-label="Blue tinted photo of a doctor with a stethoscope" style="left:0;top:0;width:134px;height:198px;background:linear-gradient(160deg,#3f7fcf,#0c55b0 60%,#0a4a9c)"></div>
      <div class="abs" style="left:8px;top:84px;width:120px;text-align:center;color:#fff;font-weight:900;font-size:11px;line-height:1.25">REVENUE CYCLE<br>MANAGEMENT</div>
      <div class="abs" style="left:122px;top:26px;width:24px;height:24px;border-radius:50%;background:#fff;box-shadow:0 0 0 3px #cfe3f4"><svg width="24" height="24" viewBox="0 0 24 24"><circle cx="12" cy="12" r="5" class="ico-b"/></svg></div>
      <p class="abs" style="left:156px;top:16px;width:186px;font-size:4.6px;line-height:1.55;color:#444">In today's increasingly complex health care environment it's important now more than ever that medical practices closely manage their revenue cycle. Bright Harbor Advisory understands the reimbursement landscape and is skilled in helping medical practices maximize reimbursement. We offer a comprehensive package of revenue cycle services including:</p>
      <ul class="abs" style="left:156px;top:76px;list-style:none;font-size:4.6px;font-weight:700;color:#444;line-height:2.35">
        <li><span style="color:var(--blue)">▶</span> Medical Billing &amp; Coding</li>
        <li><span style="color:var(--blue)">▶</span> Documentation Audit</li>
        <li><span style="color:var(--blue)">▶</span> A/R Management</li>
        <li><span style="color:var(--blue)">▶</span> Dedicated Remote Billing Manager</li>
        <li><span style="color:var(--blue)">▶</span> Dedicated Phone Number for Patients to Call</li>
        <li><span style="color:var(--blue)">▶</span> Revenue Cycle Training for Practice Staff</li>
        <li><span style="color:var(--blue)">▶</span> Credentialing</li>
        <li><span style="color:var(--blue)">▶</span> Patient Access Assessment &amp; Optimization</li>
      </ul>
    </section>

    <!-- 23 our clients -->
    <section class="slide">
      <div class="s-title">Our Clients</div>
      <div class="s-sub">SUB TITLE GOES HERE</div>
      <div class="dots"><i></i><i></i></div>
      <p class="lorem abs" style="left:130px;width:92px;top:58px;text-align:center">Lorem ipsum dolor sit amet, consectetur adipiscing elit, sed do eiusmod tempor incididunt ut labore et dolore magna aliqua. Lorem ipsum dolor sit amet, consectetur adipiscing elit.</p>
      <div class="abs bluebg" style="left:0;right:0;top:96px;bottom:0"></div>
      <svg class="abs" style="left:0;top:60px" width="352" height="110" viewBox="0 0 352 110">
        <g fill="#fff" stroke="#cfe3f4" stroke-width="3"><circle cx="60" cy="34" r="22"/><circle cx="176" cy="74" r="22"/><circle cx="292" cy="34" r="22"/></g>
        <path d="M50 38 q10 8 20 0 M54 30 l6-5 6 5" class="ico-b"/>
        <circle cx="176" cy="70" r="4" class="ico-b"/><path d="M166 80 q10 6 20 0" class="ico-b"/>
        <path d="M284 28 h16 v14 h-16z M292 31 v8 M288 35 h8" class="ico-b"/>
      </svg>
      <p class="abs" style="left:20px;top:126px;width:82px;font-size:3.8px;line-height:1.5;color:#fff;text-align:center">Lorem ipsum dolor sit amet, consectetur adipiscing elit, sed do eiusmod tempor incididunt ut labore et dolore magna aliqua. Lorem ipsum dolor sit amet, consectetur adipiscing elit.</p>
      <p class="abs" style="left:252px;top:126px;width:82px;font-size:3.8px;line-height:1.5;color:#fff;text-align:center">Lorem ipsum dolor sit amet, consectetur adipiscing elit, sed do eiusmod tempor incididunt ut labore et dolore magna aliqua. Lorem ipsum dolor sit amet, consectetur adipiscing elit.</p>
    </section>

    <!-- 24 thank you -->
    <section class="slide">
      <div class="abs bluebg" style="left:0;right:0;top:0;height:108px"></div>
      <div class="abs" style="left:28px;top:46px;color:#fff;font-weight:800;font-size:19px">THANK YOU</div>
      <div class="contact" style="top:122px"><svg width="7" height="7" viewBox="0 0 10 10"><path d="M2 1 l2 0 1 2.5 -1.3 1 q1 2 2.8 2.8 l1-1.3 2.5 1 0 2 q-5 .5-8-4.5z" fill="#555"/></svg>(555) 010-0142</div>
      <div class="contact" style="top:140px"><svg width="7" height="7" viewBox="0 0 10 10"><circle cx="5" cy="5" r="4" fill="none" stroke="#555"/><path d="M1 5 h8 M5 1 q-3 4 0 8 q3-4 0-8" fill="none" stroke="#555" stroke-width=".7"/></svg>www.website.com</div>
      <div class="contact" style="top:158px"><svg width="7" height="7" viewBox="0 0 10 10"><rect x="1" y="2" width="8" height="6" fill="#555"/><path d="M1 2 l4 3 4-3" fill="none" stroke="#fff" stroke-width=".8"/></svg>info@website.com</div>
      <div class="contact" style="top:176px"><svg width="7" height="7" viewBox="0 0 10 10"><path d="M5 9.5 q-3.5-4-3.5-5.5 a3.5 3.5 0 0 1 7 0 q0 1.5-3.5 5.5z" fill="#555"/><circle cx="5" cy="4" r="1.2" fill="#fff"/></svg>Here to write your Company adress</div>
      <div class="abs" style="left:216px;top:130px;width:112px;text-align:center;color:var(--blue);font-weight:800;font-size:20px">BHA</div>
      <div class="abs" style="left:196px;top:156px;width:152px;text-align:center;color:#666;font-size:4.6px;letter-spacing:.4px">BRIGHT HARBOR ADVISORY LLC</div>
      <div class="foot"><span class="url">www.brightharboradvisory.com</span><span class="mark">BHA</span></div>
    </section>

  </div>
</div>
</body>
</html>
```